Quimby's Yard & Garden Center Business Card Update

I need an updated Business card design for my Lawn and Garden Center. We do Landscaping installs, Lawn Mowing, Snow Removal and also have a Garden Center Retail Division. I uploaded a few of our previous business cards to give an idea of what we are starting with. The main goal of this update is to simplify and modernize the business card, not all of the services that are on the previous cards has to be on the new one but I would still like to highlight our main services. There is also a sample of our logo that Can be used in the design.

Industry/Entity Type

Landscaping

Contact Information for Business Card

Morris Quimby
Morris@Quimbysyardandgarden.example
Business (555) 201-7784
Cell (555) 318-6092

Colors

Designer to choose colors to be used in the design.

Requirements
Must have
• Services Provided :
• Landscaping
• Lawn Maintenance
• Snow Removal
• Garden Center

```html
<!DOCTYPE html>
<html lang="en">
<head>
<meta charset="utf-8">
<title>Quimby's Yard &amp; Garden Center – Business Card</title>
<link href="https://fonts.googleapis.com/css2?family=Arimo&family=Overpass:wght@700&family=Roboto+Condensed:wght@700&display=swap" rel="stylesheet">
<style>
  :root {
    --forest: #2b5b38;
    --ink: #1a1a1a;
    --paper: #ffffff;
    --edge: #8a8a8a;
  }
  * { margin: 0; padding: 0; box-sizing: border-box; }
  html, body { width: 1200px; height: 1195px; overflow: hidden; background: var(--paper); }
  .sheet { position: relative; width: 1200px; height: 1195px; }

  .card { position: absolute; left: 223px; width: 750px; height: 457px; }
  .card-front { top: 123px; background: var(--paper); border: 1px solid var(--edge); }
  .card-back { top: 611px; background: var(--forest); }

  .brand { position: absolute; display: flex; align-items: center; gap: 16px;
    font-family: "Overpass", sans-serif; font-weight: 700; }
  .brand-dot { border-radius: 50%; flex: none; }
  .card-front .brand { left: 0; right: 0; top: 190px; justify-content: center; color: var(--ink); font-size: 76px; }
  .card-front .brand-dot { width: 64px; height: 64px; background: var(--forest); }
  .card-back .brand { left: 58px; top: 130px; color: var(--paper); font-size: 56px; }
  .card-back .brand-dot { width: 48px; height: 48px; background: var(--paper); }

  .services-band { position: absolute; left: -1px; right: -1px; bottom: -1px; height: 62px;
    background: var(--forest); color: var(--paper); display: flex; align-items: center; justify-content: center;
    font-family: "Roboto Condensed", sans-serif; font-weight: 700; font-size: 20.5px; letter-spacing: 0.4px; word-spacing: 2px; }

  .contact { position: absolute; right: 56px; top: 244px; text-align: right; color: var(--paper);
    font-family: "Arimo", sans-serif; }
  .contact-name { font-family: "Overpass", sans-serif; font-weight: 700; font-size: 27px; letter-spacing: 0.5px;
    margin-right: 0; margin-bottom: 22px; }
  .contact-line { display: flex; justify-content: flex-end; align-items: center; gap: 12px; font-size: 21px;
    height: 36px; }
  .contact-line svg { width: 24px; height: 24px; flex: none; }
</style>
</head>
<body>
<div class="sheet">
  <section class="card card-front">
    <div class="brand"><span class="brand-dot"></span><span class="brand-name">Quimby's</span></div>
    <div class="services-band">Services : Landscaping &nbsp;|&nbsp; Lawn Maintenance &nbsp;|&nbsp; Snow Removal &nbsp;|&nbsp; Garden Center</div>
  </section>

  <section class="card card-back">
    <div class="brand"><span class="brand-dot"></span><span class="brand-name">Quimby's</span></div>
    <div class="contact">
      <div class="contact-name">Morris Quimby</div>
      <div class="contact-line"><span>(555) 201-7784</span>
        <svg viewBox="0 0 24 24" aria-hidden="true"><path d="M2 8c0-3 4-4 10-4s10 1 10 4v2h-5V8H7v2H2z" fill="#fff"/><path d="M6 12l2-3h8l2 3v8H6z" fill="#fff"/><g fill="#2b5b38"><circle cx="10" cy="13" r="0.9"/><circle cx="12" cy="13" r="0.9"/><circle cx="14" cy="13" r="0.9"/><circle cx="10" cy="15.5" r="0.9"/><circle cx="12" cy="15.5" r="0.9"/><circle cx="14" cy="15.5" r="0.9"/><circle cx="10" cy="18" r="0.9"/><circle cx="12" cy="18" r="0.9"/><circle cx="14" cy="18" r="0.9"/></g></svg>
      </div>
      <div class="contact-line"><span>(555) 318-6092</span>
        <svg viewBox="0 0 24 24" aria-hidden="true"><rect x="6" y="2" width="12" height="20" rx="2.5" fill="none" stroke="#fff" stroke-width="2"/><circle cx="12" cy="18.5" r="1.2" fill="#fff"/></svg>
      </div>
      <div class="contact-line"><span>Morris@Quimbysyardandgarden.example</span>
        <svg viewBox="0 0 24 24" aria-hidden="true"><rect x="2" y="5" width="20" height="14" rx="1" fill="#fff"/><path d="M2.5 5.5l9.5 8 9.5-8M2.5 18.5l7-6M21.5 18.5l-7-6" fill="none" stroke="#2b5b38" stroke-width="1.3"/></svg>
      </div>
    </div>
  </section>
</div>
</body>
</html>
```